Larkspur Advisory Biz Card Template
Corp Biz Card
Professional
Desmond Hallowell
Managing Director
desmond@larkspuradvisory-example.com
www.larkspuradvisory-example.com
Card must have bleed areas set, and sized as per the attached PDF guides.
Card should be editable for each person in company.
Our Mission:
"To assist our clients in achieving their business objectives through the successful implementation of true leading edge technology"
Services for:
* KTV Nimbus Inventory and Linkage Charting - NILC
* KTV ScriptForge - KTSF
* KTV WatchGrid
* KTV Ticket Hub Rapid
* Project Management
* Project Resourcing

```html
<!DOCTYPE html>
<html lang="en">
<head>
<meta charset="utf-8">
<title>Larkspur Advisory Stationery</title>
<link href="https://fonts.googleapis.com/css2?family=Roboto:wght@400;700&display=swap" rel="stylesheet">
<style>
:root{
  --bg:#2e2e30;
  --paper:#ffffff;
  --orange:#b9501d;
  --orange-deep:#9c4216;
  --charcoal:#3b3b3d;
  --ink:#3a3a3a;
  --muted:#8a8a8a;
  --faint-fill:#f6ece6;
  --label:#9a9a9a;
}
*{margin:0;padding:0;box-sizing:border-box}
html,body{width:1200px;height:338px;overflow:hidden;background:var(--bg);font-family:"Roboto",Arial,sans-serif}
.canvas{position:relative;width:1200px;height:338px}
.piece{position:absolute;background:var(--paper);box-shadow:0 1px 3px rgba(0,0,0,.5)}
.label{position:absolute;font-size:4px;color:var(--label);white-space:nowrap;text-align:center}
.brand{display:flex;align-items:center;gap:2px;color:var(--ink);font-weight:700;white-space:nowrap}
.brand .mark{background:var(--orange);display:inline-block;flex:none}
.band{position:absolute;left:0;right:0;background:var(--orange)}
.band-top{top:0}
.band-bottom{bottom:0}

/* business cards */
.card{width:90px;height:52px;left:22px}
.card-front{top:142px}
.card-front .brand{position:absolute;left:8px;top:20px;font-size:7px}
.card-front .brand .mark{width:6px;height:6px}
.card-back{top:226px;padding:8px 6px}
.card-back .name{font-size:4.5px;font-weight:700;color:var(--ink)}
.card-back .role{font-size:3.5px;color:var(--orange);margin-bottom:4px}
.card-back .line{font-size:3px;color:var(--muted);line-height:4.5px;white-space:nowrap}
.card .band-bottom{height:3px}

/* letterheads */
.letterhead{top:31px;width:211px;height:274px}
.letterhead-1{left:144px}
.letterhead-2{left:384px}
.letterhead .band-top{height:5px}
.letterhead .band-bottom{height:7px}
.letterhead .brand{position:absolute;left:92px;top:14px;font-size:12px}
.letterhead-2 .brand{left:62px}
.letterhead .brand .mark{width:10px;height:10px}
.letterhead .contact{position:absolute;left:26px;width:62px;top:15px;font-size:3px;color:var(--muted);line-height:4px;text-align:right;white-space:nowrap}
.letterhead .footer{position:absolute;bottom:1.5px;left:0;right:0;text-align:center;font-size:3px;color:#fff}
.watermark{position:absolute;left:70px;top:140px;width:70px;height:80px;background:var(--faint-fill)}

/* compliment slips */
.slip{left:624px;width:204px;height:103px}
.slip-1{top:41px}
.slip-2{top:180px}
.slip .band-top{height:4px}
.slip .band-bottom{height:4px}
.slip .brand{position:absolute;left:10px;top:14px;font-size:10px}
.slip .brand .mark{width:8px;height:8px}

/* envelopes */
.envelope{left:857px;width:319px;overflow:hidden}
.env-orange{top:36px;height:101px;background:var(--orange)}
.env-dark{top:137px;height:45px;background:var(--charcoal)}
.env-white{top:182px;height:122px}
.envelope svg{position:absolute;left:0;top:0}
.env-orange .brand,.env-dark .brand{position:absolute;left:152px;top:44px}
.env-dark .brand{top:14px}
.env-orange .brand .mark,.env-dark .brand .mark{width:9px;height:9px;background:#fff}
.env-white .brand{position:absolute;left:150px;top:42px;font-size:6px}
.env-white .brand .mark{width:9px;height:9px}
</style>
</head>
<body>
<main class="canvas">

  <div class="label" style="left:22px;top:134px;width:90px">Business card front</div>
  <section class="piece card card-front">
    <div class="brand"><span class="mark"></span>Larkspur Advisory</div>
    <div class="band band-bottom"></div>
  </section>

  <div class="label" style="left:22px;top:218px;width:90px">Business card back</div>
  <section class="piece card card-back">
    <p class="name">Desmond Hallowell</p>
    <p class="role">Managing Director</p>
    <p class="line">desmond@larkspuradvisory-example.com</p>
    <p class="line">www.larkspuradvisory-example.com</p>
    <div class="band band-bottom"></div>
  </section>
  <div class="label" style="left:22px;top:282px;width:90px">Business card bleed</div>

  <section class="piece letterhead letterhead-1">
    <div class="band band-top"></div>
    <div class="contact">desmond@larkspuradvisory-example.com<br>www.larkspuradvisory-example.com</div>
    <div class="brand"><span class="mark"></span>Larkspur Advisory</div>
    <div class="watermark" role="img" aria-label="Faint background brand area"></div>
    <div class="band band-bottom"></div>
    <div class="footer">www.larkspuradvisory-example.com</div>
  </section>
  <div class="label" style="left:144px;top:310px;width:211px">Letterhead page one</div>

  <section class="piece letterhead letterhead-2">
    <div class="band band-top"></div>
    <div class="brand"><span class="mark"></span>Larkspur Advisory</div>
    <div class="watermark" role="img" aria-label="Faint background brand area"></div>
    <div class="band band-bottom"></div>
    <div class="footer">www.larkspuradvisory-example.com</div>
  </section>
  <div class="label" style="left:384px;top:310px;width:211px">Letterhead page two</div>

  <section class="piece slip slip-1">
    <div class="band band-top"></div>
    <div class="brand"><span class="mark"></span>Larkspur Advisory</div>
    <div class="band band-bottom"></div>
  </section>
  <div class="label" style="left:624px;top:148px;width:204px">Compliment slip front</div>

  <section class="piece slip slip-2">
    <div class="band band-top"></div>
    <div class="brand"><span class="mark"></span>Larkspur Advisory</div>
    <div class="band band-bottom"></div>
  </section>
  <div class="label" style="left:624px;top:287px;width:204px">Compliment slip back</div>

  <section class="piece envelope env-orange">
    <svg width="319" height="101" viewBox="0 0 319 101"><polygon points="0,0 319,0 160,70" fill="var(--orange-deep)"/></svg>
    <div class="brand"><span class="mark"></span></div>
  </section>
  <section class="piece envelope env-dark">
    <svg width="319" height="45" viewBox="0 0 319 45"><polygon points="0,0 319,0 160,40" fill="#333335"/></svg>
    <div class="brand"><span class="mark"></span></div>
  </section>
  <section class="piece envelope env-white">
    <svg width="319" height="122" viewBox="0 0 319 122"><polyline points="0,0 160,60 319,0" fill="none" stroke="#e2e2e2" stroke-width="1"/></svg>
    <div class="brand"><span class="mark"></span>Larkspur Advisory</div>
  </section>
  <div class="label" style="left:857px;top:308px;width:319px">Envelope set DL</div>

</main>
</body>
</html>
```